Letterhead and Envelope Only (no biz card)
Leadership Development & Coaching Start Up
I also really like it when the swirls are not perfectly positioned on the page...bleeding off the page looks good. Thanks everyone!
Thanks for submitting your designs! Something else to keep in mind, I am rather feminine...I prefer softer lines and fainter watermarks in the background. I also really prefer the contact info to be on the bottom of the design.
Correction, I like the contact info on the bottom in #1 (not #3.)
My logo designer is out of the country, I should have those files for you in the next couple of days.
From the three designs so far, I like the swirls in #2. I like the contact info on the bottom in #3.
If possible, I'd like to have 2 letterhead designs in my winner...so I can use both for various purposes.
could you please upload the ai or eps file of logo?

```html
<!DOCTYPE html>
<html lang="en">
<head>
<meta charset="utf-8">
<title>Velmora — Letterhead and Envelope</title>
<link rel="stylesheet" href="https://fonts.googleapis.com/css2?family=Montserrat:wght@600&family=Open+Sans:wght@400&display=swap">
<style>
  :root{
    --backdrop:#a7a7a7;
    --paper:#ffffff;
    --navy:#1f3f8c;
    --sun:#f8b21a;
    --swirl:#f7e4b7;
    --ink:#3a3a3a;
    --window:#e4e4e4;
  }
  html,body{margin:0;padding:0;overflow:hidden}
  body{width:1200px;height:804px;background:var(--backdrop);position:relative;font-family:"Open Sans",Arial,sans-serif}
  .stationery{position:absolute;inset:0}
  .art{position:absolute;left:0;top:0}
  .brand{position:absolute;display:flex;align-items:center;gap:6px;margin:0;font-family:"Montserrat",Arial,sans-serif;font-weight:600;color:var(--navy);letter-spacing:.5px;line-height:1}
  .brand-dot{width:9px;height:9px;border-radius:50%;background:var(--sun)}
  .contact{position:absolute;margin:0;font-size:5.5px;line-height:1;color:var(--ink);white-space:nowrap}
  .contact span{color:var(--navy);margin:0 4px}
  .envelope-brand{left:92px;top:336px;font-size:20px}
  .envelope-contact{left:92px;top:523px}
  .letterhead-brand{left:678px;top:88px;font-size:24px}
  .letterhead-address{left:720px;width:200px;top:652px;text-align:center}
  .letterhead-contact{left:678px;top:701px}
</style>
</head>
<body>
<main class="stationery">

  <svg class="art" width="1200" height="804">
    <defs>
      <radialGradient id="swirlGlow">
        <stop offset="0" stop-color="#f7e4b7" stop-opacity=".75"/>
        <stop offset="1" stop-color="#f7e4b7" stop-opacity="0"/>
      </radialGradient>
      <clipPath id="envClip"><rect x="65" y="312" width="498" height="240"/></clipPath>
      <clipPath id="sheetClip"><rect x="643" y="43" width="509" height="706"/></clipPath>
    </defs>

    <!-- Envelope -->
    <path class="envelope-flap" d="M65 312 C80 280 120 220 200 212 L430 212 C500 218 540 280 563 312 Z" fill="var(--navy)"/>
    <rect class="envelope-body" x="65" y="312" width="498" height="240" fill="var(--paper)"/>
    <rect x="65" y="312" width="498" height="3" fill="var(--sun)"/>
    <g clip-path="url(#envClip)">
      <circle role="img" aria-label="faint swirl watermark" cx="520" cy="360" r="55" fill="url(#swirlGlow)"/>
      <circle role="img" aria-label="faint swirl watermark" cx="430" cy="470" r="50" fill="url(#swirlGlow)"/>
      <circle role="img" aria-label="faint swirl watermark" cx="345" cy="515" r="32" fill="url(#swirlGlow)"/>
      <circle class="sun-corner" cx="563" cy="552" r="78" fill="var(--sun)"/>
    </g>
    <rect class="envelope-window" x="187" y="398" width="173" height="75" rx="4" fill="var(--window)" stroke="#d0d0d0"/>
    <rect x="65" y="536" width="470" height="2" fill="var(--navy)"/>

    <!-- Letterhead -->
    <rect class="letterhead-sheet" x="643" y="43" width="509" height="706" fill="var(--paper)"/>
    <rect x="643" y="43" width="509" height="4" fill="var(--sun)"/>
    <g clip-path="url(#sheetClip)">
      <circle role="img" aria-label="faint swirl watermark" cx="720" cy="470" r="150" fill="url(#swirlGlow)"/>
      <circle role="img" aria-label="faint swirl watermark" cx="1060" cy="285" r="120" fill="url(#swirlGlow)"/>
      <circle role="img" aria-label="faint swirl watermark" cx="1020" cy="585" r="75" fill="url(#swirlGlow)"/>
      <circle role="img" aria-label="faint swirl watermark" cx="850" cy="650" r="70" fill="url(#swirlGlow)"/>
      <circle class="sun-corner" cx="1152" cy="749" r="90" fill="var(--sun)"/>
    </g>
    <rect x="660" y="714" width="470" height="2" fill="var(--navy)"/>
  </svg>

  <p class="brand envelope-brand">Velmora<i class="brand-dot"></i></p>
  <p class="contact envelope-contact">1420 Lakeview Drive, Brenton, OR 97321<span>|</span>P<span>|</span>541.620.4178<span>|</span>www.velmoragroup.com</p>

  <p class="brand letterhead-brand">Velmora<i class="brand-dot"></i></p>
  <p class="contact letterhead-address">1420 Lakeview Drive, Brenton, OR 97321</p>
  <p class="contact letterhead-contact">P<span>|</span>541.620.4178<span>|</span>hello@velmoragroup.com<span>|</span>www.velmoragroup.com</p>

</main>
</body>
</html>
```